Brambel Logging Business Card Design Project

We need a new company business card. We provide professional timber harvesting (logging) and forest management services. I'm open to any creative design. Most company caps and shirts are navy blue and Light grey. Logo does not necessarily have to contain those colors. Logo containing picture of logging equipment, log truck, trees, or logs are acceptable. Be creative. Final logo should communicate our company's pride and professionalism in the East Texas Timber Industry.
Updates

Target Market(s)

Timber owners, sawmills, and forestry professionals

Industry/Entity Type

Business

Requirements
Must have
• Must have Contact Info.
Phone: 936-402-5817
address: PO Box 8462
New Waverly, Tx 77358
www.mbrambellogging.example
mbrambellogging@mailbox.example
Owner: Marv Brambel

Or design must leave room for this info.

```html
<!DOCTYPE html>
<html lang="en">
<head>
<meta charset="utf-8">
<title>Brambel Logging – Business Card</title>
<link href="https://fonts.googleapis.com/css2?family=Oswald:wght@500&family=Ubuntu:wght@400;700&display=swap" rel="stylesheet">
<style>
  :root{
    --yellow:#f8b526;
    --black:#1e1e1e;
    --charcoal:#3a3a3a;
    --grey:#c9c9c9;
    --paper:#f7f7f7;
    --paper-edge:#dcdcdc;
    --stage:#ebe7df;
    --white:#ffffff;
  }
  *{box-sizing:border-box;margin:0;padding:0}
  html,body{width:1057px;height:1200px;overflow:hidden;background:var(--stage)}
  body{position:relative;font-family:"Ubuntu",sans-serif;color:var(--charcoal)}

  .card{position:absolute;left:108px;width:840px;height:480px;overflow:hidden;
        box-shadow:0 10px 28px rgba(0,0,0,.22)}
  .card--front{top:60px;background:var(--yellow);padding:16px}
  .card--back{top:660px;background:radial-gradient(ellipse at 35% 35%,var(--white) 0%,var(--paper) 45%,var(--paper-edge) 100%)}

  .front-frame{width:100%;height:100%;background:var(--black);padding:10px}
  .front-face{position:relative;width:100%;height:100%;
        background:radial-gradient(ellipse at 45% 40%,var(--white) 0%,var(--paper) 50%,var(--paper-edge) 100%)}

  .brand{position:absolute;display:flex;align-items:center;gap:22px}
  .brand-mark{width:74px;height:74px;border-radius:50%;background:var(--yellow);flex:none}
  .brand-name{font-weight:700;color:var(--charcoal);line-height:1.05;white-space:nowrap}
  .card--front .brand{left:170px;top:150px}
  .card--front .brand-name{font-size:46px}
  .card--back .brand{left:60px;top:70px;gap:16px}
  .card--back .brand-mark{width:56px;height:56px}
  .card--back .brand-name{font-size:34px}

  .back-shapes{position:absolute;inset:0}

  .person{position:absolute;left:60px;top:288px}
  .person-name{font-family:"Oswald",sans-serif;font-weight:500;font-size:34px;letter-spacing:2px;color:var(--black);line-height:1}
  .person-role{font-size:16px;letter-spacing:4px;color:var(--black);margin-top:6px}

  .contact-list{position:absolute;list-style:none;display:flex;flex-direction:column;gap:9px}
  .contact-list--address{left:60px;top:378px}
  .contact-list--phone{left:560px;top:160px}
  .contact-item{display:flex;align-items:center;gap:12px;font-size:14px;color:var(--black);white-space:nowrap}
  .contact-list--phone .contact-item{color:var(--white);font-size:14px}
  .contact-icon{width:22px;height:22px;background:var(--black);display:flex;align-items:center;justify-content:center;flex:none}
  .contact-list--phone .contact-icon{background:var(--white)}
</style>
</head>
<body>

<section class="card card--front" aria-label="Business card front">
  <div class="front-frame">
    <div class="front-face">
      <div class="brand">
        <span class="brand-mark"></span>
        <p class="brand-name">Marv Brambel<br>Brambel Logging</p>
      </div>
    </div>
  </div>
</section>

<section class="card card--back" aria-label="Business card back">
  <svg class="back-shapes" width="840" height="480" viewBox="0 0 840 480" aria-hidden="true">
    <polygon points="520,80 840,80 840,150 490,150" fill="#c9c9c9"/>
    <polygon points="490,150 840,150 840,232 450,232" fill="#1e1e1e"/>
    <polygon points="0,268 560,268 470,480 0,480" fill="#f8b526"/>
    <polygon points="560,268 590,268 500,480 470,480" fill="#1e1e1e"/>
  </svg>

  <div class="brand">
    <span class="brand-mark"></span>
    <p class="brand-name">Marv Brambel<br>Brambel Logging</p>
  </div>

  <div class="person">
    <p class="person-name">MARV BRAMBEL</p>
    <p class="person-role">FOUNDER</p>
  </div>

  <ul class="contact-list contact-list--phone">
    <li class="contact-item">
      <span class="contact-icon"><svg width="12" height="12" viewBox="0 0 12 12"><path d="M2 1h2.5l1 2.5-1.5 1a6 6 0 0 0 3.5 3.5l1-1.5L11 7.5V10a1 1 0 0 1-1 1A9 9 0 0 1 1 2a1 1 0 0 1 1-1z" fill="#1e1e1e"/></svg></span>
      (555) 010-0147
    </li>
    <li class="contact-item">
      <span class="contact-icon"><svg width="12" height="12" viewBox="0 0 12 12"><path d="M2 1h2.5l1 2.5-1.5 1a6 6 0 0 0 3.5 3.5l1-1.5L11 7.5V10a1 1 0 0 1-1 1A9 9 0 0 1 1 2a1 1 0 0 1 1-1z" fill="#1e1e1e"/></svg></span>
      (555) 010-0182
    </li>
  </ul>

  <ul class="contact-list contact-list--address">
    <li class="contact-item">
      <span class="contact-icon"><svg width="12" height="12" viewBox="0 0 12 12"><path d="M6 1a3.5 3.5 0 0 1 3.5 3.5C9.5 7 6 11 6 11S2.5 7 2.5 4.5A3.5 3.5 0 0 1 6 1z" fill="#fff"/><circle cx="6" cy="4.5" r="1.2" fill="#1e1e1e"/></svg></span>
      PO Box 0000, Sampleton, ST 00000
    </li>
    <li class="contact-item">
      <span class="contact-icon"><svg width="12" height="12" viewBox="0 0 12 12"><circle cx="6" cy="6" r="4.5" fill="none" stroke="#fff" stroke-width="1.2"/><path d="M1.5 6h9M6 1.5c-2 2.5-2 6.5 0 9M6 1.5c2 2.5 2 6.5 0 9" fill="none" stroke="#fff" stroke-width="1"/></svg></span>
      www.mbrambellogging.example
    </li>
    <li class="contact-item">
      <span class="contact-icon"><svg width="12" height="12" viewBox="0 0 12 12"><rect x="1" y="2.5" width="10" height="7" fill="none" stroke="#fff" stroke-width="1.2"/><path d="M1 3l5 4 5-4" fill="none" stroke="#fff" stroke-width="1.2"/></svg></span>
      mbrambellogging@mailbox.example
    </li>
  </ul>
</section>

</body>
</html>
```